Aerial photo/video drone company needs new business card

Aerial visual company who offers photos and video services via drones.

We are QVL certified and work in the real estate, insurance, construction, and film industries.

I'm looking for a clean, professional, maybe even edgy design, that will be a conversation starter when networking.

I've included our logo, current business card, and font.

Our current business card is decent; albeit, I'm looking for something more unique. If you folks provide good designs, I'll definitely guarantee payment (and I'm not opposed to tipping if the design is above and beyond).

Target Market(s)

Insurance companies, real estate agents, construction companies, advertising & other creative agencies, and filmmakers/producers.

Industry/Entity Type

Business

Contact Information for Business Card

Company name pronounced air-a-vee.

Font styles to use
Other font styles liked:
• Font was uploaded; that or similar; not opposed to other fonts if they work well with the design

Requirements
Must have
• Clearly prominent logo; my name and title; phone number; email address; web address; mentioned "QVL Certified" or similar; should indicate "Aerial visual"
Nice to have
• Watermark of logo or otherwise
Should not have
• Pictures of drones or scenic shots

```html
<!DOCTYPE html>
<html lang="en">
<head>
<meta charset="utf-8">
<title>Skyvane Business Card</title>
<link rel="stylesheet" href="https://fonts.googleapis.com/css2?family=Montserrat:wght@500;600;700&display=swap">
<style>
  :root {
    --page-bg: #3b3540;
    --card-bg: #ffffff;
    --navy: #2b4566;
    --sky: #1a9be3;
    --ink: #111111;
    --muted: #5a6675;
    --divider: #d6d6d6;
  }
  * { margin: 0; padding: 0; box-sizing: border-box; }
  html, body { width: 1200px; height: 800px; overflow: hidden; }
  body {
    background: var(--page-bg);
    font-family: "Montserrat", Arial, sans-serif;
    position: relative;
  }
  .card {
    position: absolute;
    left: 320px;
    width: 560px;
    height: 320px;
    background: var(--card-bg);
    box-shadow: 0 10px 30px rgba(0,0,0,0.35);
  }
  .card--front { top: 60px; }
  .card--back { top: 420px; }

  .wordmark {
    display: flex;
    align-items: center;
    gap: 14px;
    color: var(--navy);
    font-weight: 700;
    letter-spacing: 1px;
  }
  .wordmark__dot {
    border-radius: 50%;
    background: var(--sky);
    flex: none;
  }
  .card--front .wordmark {
    position: absolute;
    inset: 0;
    justify-content: center;
    font-size: 84px;
  }
  .card--front .wordmark__dot { width: 48px; height: 48px; }

  .brand {
    position: absolute;
    left: 32px;
    top: 122px;
    width: 222px;
  }
  .card--back .wordmark {
    font-size: 38px;
    gap: 10px;
    line-height: 1;
  }
  .card--back .wordmark__dot { width: 22px; height: 22px; }
  .brand__tagline {
    margin-top: 12px;
    font-size: 10px;
    font-weight: 600;
    letter-spacing: 1.5px;
    text-transform: uppercase;
    color: var(--muted);
    line-height: 1.6;
  }
  .brand__tagline strong { color: var(--sky); font-weight: 600; }

  .divider {
    position: absolute;
    left: 262px;
    top: 48px;
    width: 2px;
    height: 224px;
    background: linear-gradient(to bottom, transparent, var(--divider) 20%, var(--divider) 80%, transparent);
  }
  .contact {
    position: absolute;
    left: 292px;
    top: 62px;
  }
  .contact__name {
    color: var(--sky);
    font-size: 24px;
    font-weight: 600;
  }
  .contact__title {
    color: var(--ink);
    font-size: 12px;
    font-weight: 600;
    margin: 2px 0 18px;
  }
  .contact__list { list-style: none; }
  .contact__item {
    display: flex;
    align-items: center;
    gap: 12px;
    font-size: 14px;
    font-weight: 600;
    color: var(--ink);
    margin-bottom: 12px;
  }
  .contact__icon {
    width: 28px;
    height: 28px;
    border-radius: 50%;
    background: var(--ink);
    display: flex;
    align-items: center;
    justify-content: center;
    flex: none;
  }
  .contact__icon svg { width: 16px; height: 16px; }
</style>
</head>
<body>
  <section class="card card--front">
    <div class="wordmark"><span class="wordmark__dot"></span>skyvane</div>
  </section>

  <section class="card card--back">
    <div class="brand">
      <div class="wordmark"><span class="wordmark__dot"></span>skyvane</div>
      <p class="brand__tagline">Aerial Visual<br><strong>QVL Certified</strong></p>
    </div>
    <div class="divider"></div>
    <div class="contact">
      <p class="contact__name">Daniel T. Marlow</p>
      <p class="contact__title">Owner</p>
      <ul class="contact__list">
        <li class="contact__item">
          <span class="contact__icon">
            <svg viewBox="0 0 16 16"><path d="M4 2 L6.5 2 L7.5 5 L6 6.2 C6.8 8 8 9.2 9.8 10 L11 8.5 L14 9.5 L14 12 C14 13 13 14 12 14 C6.5 13.5 2.5 9.5 2 4 C2 3 3 2 4 2 Z" fill="#fff"/></svg>
          </span>
          555 014 2870
        </li>
        <li class="contact__item">
          <span class="contact__icon">
            <svg viewBox="0 0 16 16"><rect x="2" y="4" width="12" height="8" fill="none" stroke="#fff" stroke-width="1.4"/><path d="M2 4 L8 9 L14 4" fill="none" stroke="#fff" stroke-width="1.4"/></svg>
          </span>
          dan@skyvane.com
        </li>
        <li class="contact__item">
          <span class="contact__icon">
            <svg viewBox="0 0 16 16"><circle cx="8" cy="8" r="6" fill="none" stroke="#fff" stroke-width="1.4"/><ellipse cx="8" cy="8" rx="2.6" ry="6" fill="none" stroke="#fff" stroke-width="1.2"/><path d="M2 8 H14" stroke="#fff" stroke-width="1.2"/></svg>
          </span>
          skyvane.com
        </li>
      </ul>
    </div>
  </section>
</body>
</html>
```